Business Card Design Project

Same as the logo requirements.
Address of the store is:
Milo's Junction, LLC
287B North Linden Ave Suite 4
Halden, KY 44697
Gerald Pemberton, Owner
Updates

Project Deadline Extended
Reason: The design of the business cards should be the same as the main logo.

Project Deadline Extended
Reason: I approved the wrong design!

This is the link to the current logo design: http://files.artbinhub.net/img_store/273915/604128/604128_9275031_273915_pic.jpg

Target Market(s)

Courthouse and downtown employees, including lawyers, judges, downtown office workers.

Industry/Entity Type

Store

Font styles to use
Serif

Requirements
Must have
• Milo's Junction
A Corner Market, and Beyond, by Lantern Plaza!
Halden, KY 44697
Nice to have
• Colorful, Arrow sign

```html
<!DOCTYPE html>
<html lang="en">
<head>
<meta charset="utf-8">
<title>Milo's Junction, LLC — Business Card</title>
<link rel="stylesheet" href="https://fonts.googleapis.com/css2?family=Cinzel:wght@400;500&family=Libre+Baskerville:wght@400;700&display=swap">
<style>
  :root {
    --page-bg: #e9e7e3;
    --card-bg: #ffffff;
    --brand-blue: #2f4b93;
    --band-grey: #7b7b7b;
    --arrow-dark: #3b3b3b;
    --role-grey: #555555;
    --band-text: #ffffff;
  }
  * { margin: 0; padding: 0; box-sizing: border-box; }
  html, body {
    width: 1200px;
    height: 800px;
    overflow: hidden;
    background: var(--page-bg);
  }
  .canvas {
    width: 1200px;
    height: 800px;
    display: flex;
    align-items: center;
    justify-content: center;
  }
  .business-card {
    position: relative;
    width: 1050px;
    height: 600px;
    background: var(--card-bg);
    box-shadow: 0 6px 24px rgba(0,0,0,0.12);
    overflow: hidden;
  }
  .brand {
    position: absolute;
    top: 120px;
    left: 0;
    width: 100%;
    display: flex;
    justify-content: center;
    align-items: center;
    gap: 26px;
  }
  .brand-name {
    font-family: "Cinzel", serif;
    font-weight: 400;
    font-size: 60px;
    letter-spacing: 1px;
    color: var(--brand-blue);
    line-height: 1.2;
  }
  .brand-dot {
    width: 46px;
    height: 46px;
    border-radius: 50%;
    background: var(--brand-blue);
  }
  .arrow {
    position: absolute;
    width: 30px;
    height: 40px;
  }
  .arrow-to-owner { top: 205px; left: 365px; }
  .arrow-to-address { top: 335px; left: 300px; }
  .owner {
    position: absolute;
    top: 250px;
    left: 0;
    width: 100%;
    text-align: center;
  }
  .owner-name {
    font-family: "Cinzel", serif;
    font-weight: 400;
    font-size: 48px;
    color: var(--brand-blue);
    line-height: 1;
  }
  .owner-role {
    font-family: "Libre Baskerville", serif;
    font-size: 22px;
    color: var(--role-grey);
    margin-top: 6px;
    margin-right: 150px;
  }
  .address-band {
    position: absolute;
    left: 0;
    top: 400px;
    width: 100%;
    height: 120px;
    background: var(--band-grey);
    display: flex;
    align-items: center;
    padding-left: 70px;
  }
  .address {
    font-family: "Libre Baskerville", serif;
    font-weight: 700;
    font-size: 30px;
    letter-spacing: 1px;
    color: var(--band-text);
    white-space: nowrap;
  }
</style>
</head>
<body>
<main class="canvas">
  <article class="business-card">
    <header class="brand">
      <h1 class="brand-name">Milo's Junction, LLC</h1>
      <span class="brand-dot" aria-hidden="true"></span>
    </header>

    <svg class="arrow arrow-to-owner" viewBox="0 0 30 40" aria-hidden="true">
      <path d="M15 2 V30 M5 22 L15 34 L25 22" fill="none" stroke="var(--arrow-dark)" stroke-width="5" stroke-linecap="round" stroke-linejoin="round"/>
    </svg>

    <section class="owner">
      <h2 class="owner-name">Gerald Pemberton</h2>
      <p class="owner-role">Owner</p>
    </section>

    <svg class="arrow arrow-to-address" viewBox="0 0 30 40" aria-hidden="true">
      <path d="M15 2 V30 M5 22 L15 34 L25 22" fill="none" stroke="var(--arrow-dark)" stroke-width="5" stroke-linecap="round" stroke-linejoin="round"/>
    </svg>

    <footer class="address-band">
      <p class="address">287B North Linden Ave Suite 4 Halden, KY 44697</p>
    </footer>
  </article>
</main>
</body>
</html>
```